International Psychology Practitioner, Educator and Researcher

I need a new website (or upgrade from existing square space. I provide innovative, client focused, services that are evidence based, specializing in crisis intervention, addiction and other mental health. I am also a researcher and university professor committed to excellence in education. I’m building on an existing practice (www.tidewellpath.ca) and incorporating my personal/professional grade. I would like to see designs that use neutral colours and that incorporate crisp clear lines in a professional and inviting way. The final design should communicate professionalism and approachability. (New head shots and stills to follow)

Target Market(s)

Seeking therapy

Industry/Entity Type

Psychology

Coding

Coded - Design and coding required

Number of Pages Required

3 page

Font styles to use
Sans Serif

Requirements
Must have
• A friendly, warm, crisp feel - professional
Nice to have
• Each tones

```html
<!DOCTYPE html>
<html lang="en">
<head>
<meta charset="utf-8">
<title>TidewellPath.ca — Coaching &amp; Psychology</title>
<link href="https://fonts.googleapis.com/css2?family=Cabin:ital,wght@0,400;0,500;0,600;1,400&display=swap" rel="stylesheet">
<style>
:root{
  --peach:#fdeee6;
  --coral:#ef8c7f;
  --ink:#2b2b2b;
  --text:#555;
  --muted:#777;
  --nav:rgba(40,40,40,.82);
  --white:#fff;
  --line:#e4e4e4;
}
*{box-sizing:border-box;margin:0;padding:0}
html,body{width:1200px;height:3841px;overflow:hidden}
body{position:relative;background:var(--white);font-family:"Cabin",sans-serif;color:var(--ink)}
.abs{position:absolute}
.social{display:flex;gap:7px}
.social span{width:38px;height:38px;border:1.5px solid var(--ink);border-radius:50%;display:block;position:relative}
.social span::after{content:"";position:absolute;left:50%;top:50%;width:8px;height:8px;background:var(--ink);border-radius:50%;transform:translate(-50%,-50%)}
.btn{position:absolute;display:flex;align-items:center;justify-content:center;font-size:15px;letter-spacing:.2px;color:var(--ink)}
.btn-outline{border:1.5px solid var(--ink);border-radius:18px 0 18px 0;background:transparent}
.btn-soft{background:var(--peach);border-radius:18px;box-shadow:0 3px 8px rgba(0,0,0,.12)}

/* header */
.topbar{left:0;top:0;width:1200px;height:100px;background:var(--peach)}
.brand{left:0;width:1200px;top:30px;text-align:center;font-size:34px;font-weight:400;color:var(--ink)}
.hero-photo{left:0;top:100px;width:1200px;height:745px;background:linear-gradient(120deg,#e9e6e1 0%,#d8d2c8 45%,#b98f78 70%,#ede9e3 100%)}
.nav{left:0;top:100px;width:1200px;height:53px;background:var(--nav);display:flex;justify-content:center;gap:38px;align-items:center;color:var(--white);font-size:15px;font-weight:500}
.hero-band{left:188px;top:720px;width:1012px;height:207px;background:var(--coral);border-top-left-radius:90px;border-top:6px solid var(--white);border-left:6px solid var(--white)}
.hero-title{left:249px;top:758px;font-size:52px;line-height:70px;color:var(--white);font-weight:500}
.dot-arrow{width:38px;height:38px;border-radius:50%;background:var(--white);display:flex;align-items:center;justify-content:center}

/* about */
.about-photo{left:113px;top:1010px;width:456px;height:425px;border-radius:10px;box-shadow:0 4px 14px rgba(0,0,0,.18);background:linear-gradient(135deg,#8a5a45 0%,#d9d2c7 40%,#e9573a 62%,#f0ece6 100%)}
.section-title{font-size:33px;font-weight:500;color:var(--ink)}
.copy{font-size:13px;line-height:28px;color:var(--text)}

/* dream */
.dream{left:0;top:1523px;width:1200px;height:391px;background:linear-gradient(180deg,#b9c1b6 0%,#c9c7b2 60%,#a68a6c 100%)}
.dream-text{left:112px;top:1608px;font-size:32px;line-height:60px;font-weight:600;color:#333}

/* services */
.svc-main{left:104px;top:2166px;width:318px;height:498px;border-radius:10px;box-shadow:0 4px 14px rgba(0,0,0,.18);background:linear-gradient(160deg,#cfcbc4 0%,#8e8a85 55%,#55504b 100%)}
.svc-card{top:2422px;width:215px;height:242px;border-radius:8px;overflow:hidden;box-shadow:0 3px 10px rgba(0,0,0,.15)}
.svc-card .pic{height:187px}
.svc-card .label{height:55px;background:var(--coral);color:var(--white);font-size:15px;padding:18px 12px}

/* testimonial */
.pattern{left:0;top:2747px;width:1200px;height:656px;background:#ededed}
.quote-card{left:173px;top:2837px;width:428px;height:383px;background:var(--white);box-shadow:0 4px 14px rgba(0,0,0,.1)}
.quote-photo{left:601px;top:2792px;width:426px;height:428px;background:linear-gradient(180deg,#ededed 0%,#ededed 10%,#f3a23b 10%,#f09a32 100%)}
.quote{left:227px;top:2925px;font-size:33px;line-height:47px;font-style:italic;color:#333}

/* cta */
.cta{left:0;top:3306px;width:1029px;height:206px;background:var(--coral);border-top-right-radius:80px;box-shadow:6px -6px 0 var(--white),8px -8px 0 #f1c3ba}
.cta-title{left:110px;top:3340px;font-size:68px;font-style:italic;color:var(--white)}
.cta-sub{left:110px;top:3428px;font-size:32px;color:var(--white)}

/* footer */
.foot-h{font-size:19px;color:var(--ink)}
.foot-t{font-size:14px;line-height:27px;color:var(--text)}
.foot-t svg{vertical-align:-2px;margin-right:6px}
.divider{left:104px;top:3739px;width:984px;height:1px;background:var(--line)}
</style>
</head>
<body>

<header>
  <div class="abs topbar"></div>
  <div class="abs social" style="left:112px;top:32px" aria-label="Social links"><span></span><span></span><span></span></div>
  <div class="abs brand">TidewellPath.ca</div>
  <div class="btn btn-outline" style="left:932px;top:28px;width:155px;height:52px">CONTACT US</div>
</header>

<section class="hero">
  <div class="abs hero-photo" role="img" aria-label="Photo of a coach in conversation with a smiling client on a white sofa"></div>
  <nav class="abs nav"><span>HOME</span><span>ABOUT US</span><span>OUR SERVICES</span><span>CORPORATE CLIENTS</span></nav>
  <div class="abs hero-band"></div>
  <h1 class="abs hero-title">GET READY TO TAKE CONTROL<br>OF YOUR LIFE.</h1>
  <div class="btn btn-soft" style="left:869px;top:842px;width:309px;height:60px">SCHEDULE A CONSULTATION TODAY</div>
  <div class="abs dot-arrow" style="left:1069px;top:699px"><svg width="10" height="12"><path d="M7 1L2 6l5 5" fill="none" stroke="#ef8c7f" stroke-width="1.5"/></svg></div>
  <div class="abs dot-arrow" style="left:1114px;top:699px"><svg width="10" height="12"><path d="M3 1l5 5-5 5" fill="none" stroke="#ef8c7f" stroke-width="1.5"/></svg></div>
</section>

<section class="about">
  <div class="abs about-photo" role="img" aria-label="Photo of a coach in a red dress with glasses talking with a client"></div>
  <h2 class="abs section-title" style="left:622px;top:1038px">ABOUT US</h2>
  <svg class="abs" style="left:620px;top:1074px" width="200" height="12"><path d="M2 8 Q100 2 196 6" fill="none" stroke="#222" stroke-width="2.2" stroke-linecap="round"/></svg>
  <p class="abs copy" style="left:622px;top:1114px;width:460px">We are a specialized boutique firm providing qualified, evidence, and compassionate services online and in person.&nbsp; We embrace a safe, holistic and trauma informed method that is uniquely designed to motivate you to make the changes you want to make</p>
  <p class="abs copy" style="left:622px;top:1243px;width:460px">Whether it's life, relationship, career or conflict - our certified and highly trained practitioners are here to support you to achieve your goals and maximize your performance in all aspects of life.</p>
  <div class="btn btn-outline" style="left:623px;top:1350px;width:155px;height:53px">READ MORE</div>
</section>

<section class="abs dream" role="img" aria-label="Photo of a woman with raised arms standing on a rock above the sea at dusk"></section>
<p class="abs dream-text">DREAM BIG.<br>DO WHAT'S RIGHT NOT WHAT'S EASY.<br>FINISH WHAT YOU START.</p>
<svg class="abs" style="left:110px;top:1796px" width="516" height="22"><path d="M3 16 Q250 2 512 6" fill="none" stroke="#111" stroke-width="4" stroke-linecap="round"/></svg>

<section class="services">
  <h2 class="abs section-title" style="left:113px;top:1998px">OUR SERVICES</h2>
  <svg class="abs" style="left:111px;top:2050px" width="234" height="14"><path d="M2 10 Q115 2 230 6" fill="none" stroke="#222" stroke-width="2.2" stroke-linecap="round"/></svg>
  <p class="abs" style="left:114px;top:2080px;font-size:18px;line-height:30px;color:var(--text)">Lorem ipsum dolor sit amet, consectetur<br>adipiscing elit, sed do</p>
  <div class="abs svc-main" role="img" aria-label="Photo of two women talking at a table by a window"></div>
  <h3 class="abs" style="left:444px;top:2180px;font-size:30px;font-weight:400;color:#555">Master Life Coaching.</h3>
  <p class="abs copy" style="left:444px;top:2227px;width:640px;line-height:30px">A results based life coach is someone who helps you identify your goals and develop an actionable plan to achieve them. We If you want to get to the next level in life we provide enthusiastic support, objective perspectives and work with you to find practical solutions to complex issues.</p>
  <div class="btn btn-outline" style="left:447px;top:2334px;width:155px;height:52px">READ MORE</div>
  <div class="abs svc-card" style="left:438px"><div class="pic" role="img" aria-label="Photo of a smiling couple in a session" style="background:linear-gradient(135deg,#e8e4dc,#6f88a8 60%,#3a2f2a)"></div><div class="label">Relationship Coaching.</div></div>
  <div class="abs svc-card" style="left:665px"><div class="pic" role="img" aria-label="Photo of two women reviewing work at a desk" style="background:linear-gradient(135deg,#dfe3e6,#9aa3a8 55%,#4b4a48)"></div><div class="label">Career Coaching.</div></div>
  <div class="abs svc-card" style="left:891px"><div class="pic" role="img" aria-label="Photo of two men talking in an office lounge" style="background:linear-gradient(135deg,#eceae6,#b7b4ad 55%,#5f6670)"></div><div class="label">Psychometric Profiles.</div></div>
  <div class="abs dot-arrow" style="left:1117px;top:2515px;border:1px solid #ddd"><svg width="12" height="12"><path d="M1 6h9M6 2l4 4-4 4" fill="none" stroke="#333" stroke-width="1.8"/></svg></div>
</section>

<section class="testimonial">
  <div class="abs pattern" role="img" aria-label="Soft light grey decorative background"></div>
  <div class="abs quote-card"></div>
  <svg class="abs" style="left:227px;top:2866px" width="24" height="20"><path d="M1 19V10Q1 2 10 1v4Q5 6 5 10h5v9zM14 19V10q0-8 9-9v4q-5 1-5 5h5v9z" fill="#ef8c7f"/></svg>
  <p class="abs quote">I dreamed big! I'm now in my<br>dream career living my<br>best life</p>
  <p class="abs quote" style="top:3094px;font-size:24px;left:232px">— Maren T.</p>
  <div class="abs quote-photo" role="img" aria-label="Portrait photo of a smiling client in a leather jacket against an orange wall"></div>
</section>

<section class="cta-block">
  <div class="abs cta"></div>
  <h2 class="abs cta-title">Let's Talk!</h2>
  <p class="abs cta-sub">Your first discovery consultation is free.</p>
  <div class="btn btn-soft" style="left:656px;top:3381px;width:307px;height:59px">SCHEDULE A CONSULTATION TODAY</div>
</section>

<footer>
  <h4 class="abs foot-h" style="left:113px;top:3580px;font-weight:400">Location</h4>
  <p class="abs foot-t" style="left:115px;top:3620px"><svg width="10" height="14"><path d="M5 13C2 9 1 7 1 5a4 4 0 018 0c0 2-1 4-4 8z" fill="none" stroke="#ef8c7f" stroke-width="1.5"/><circle cx="5" cy="5" r="1.4" fill="#ef8c7f"/></svg>1-508 Harbourview Lane<br>Ashcombe, BC, Canada</p>
  <h4 class="abs foot-h" style="left:481px;top:3580px;font-weight:400">Hours</h4>
  <p class="abs foot-t" style="left:483px;top:3620px"><svg width="13" height="13"><circle cx="6.5" cy="6.5" r="5.5" fill="none" stroke="#ef8c7f" stroke-width="1.4"/><path d="M6.5 3.5v3l2 1.5" fill="none" stroke="#ef8c7f" stroke-width="1.4"/></svg>Monday — Friday 9am — 5pm<br><span style="padding-left:18px">Saturday&nbsp; 9am — 1pm</span></p>
  <h4 class="abs foot-h" style="left:869px;top:3580px;font-weight:400">Contact</h4>
  <p class="abs foot-t" style="left:871px;top:3620px"><svg width="14" height="11"><rect x="1" y="1" width="12" height="9" fill="#ef8c7f"/><path d="M1 1l6 5 6-5" fill="none" stroke="#fff" stroke-width="1.2"/></svg>hello@tidewellpath.ca<br><svg width="13" height="13"><path d="M3 1l2 3-1.5 1.5q1.5 3 4 4L9 8l3 2-1.5 2.5Q5 12 1 3z" fill="#ef8c7f"/></svg>(250) 555-0147<br><span style="color:var(--coral);text-decoration:underline">Schedule an Appointment</span></p>
  <div class="abs divider"></div>
  <p class="abs" style="left:111px;top:3776px;font-size:14px;color:var(--text)">© 2021 All Rights Reserved</p>
  <div class="abs social" style="left:959px;top:3767px" aria-label="Social links"><span></span><span></span><span></span></div>
</footer>

</body>
</html>
```